Beacon Lending. We focus on mentoring our clients into a home. Partner Beacon Realty Group

Needing a Mortgage Company Website. We would like a mortgage calculator on the site as well as it linked to our partner sites.

We have 6 Other Websites that go into this.

We focus on helping our clients get approved for a home. We would like a mortgage calculator on it.
See other sites
www.harborvalehomes.example
www.keystepready.example

Target Market(s)

Modern, Average guy.

Industry/Entity Type

Mortgage Brokerage

Number of Pages Required

4 page

Font styles to use
Serif
Sans Serif

Colors
000000
0255a3
33a6d7

Requirements
Must have
• Plugins, Calculator, nice design, Contact form, SEO capability, etc.
Nice to have
• Someone I can hire for our 547 other sites. Finding a good designer is difficult and we have about 3 years worth of work.
Should not have
• You can pick the colors. Just Had some ideas. Please feel free to adjust it to your liking, You are the pro..
• We just want a nice clean friendly site we can capture leads on. We want to link our other companies and also Provide them worth Education and Tools to get approved for loan

```html
<!DOCTYPE html>
<html lang="en">
<head>
<meta charset="utf-8">
<title>Beacon Lending</title>
<link href="https://fonts.googleapis.com/css2?family=Open+Sans:wght@400;600;700&display=swap" rel="stylesheet">
<style>
:root{
  --navy:#0a3c8f;
  --blue:#1565c0;
  --sky:#2e8fd3;
  --band:#1f6fd0;
  --footer:#0c3f9c;
  --ink:#222;
  --muted:#555;
  --white:#fff;
  --line:#c9c9c9;
  --dark:#2b2b2b;
}
*{box-sizing:border-box;margin:0;padding:0}
html,body{width:1200px;height:3352px;overflow:hidden}
body{position:relative;font-family:"Open Sans",Arial,sans-serif;color:var(--ink);background:var(--white)}
.abs{position:absolute}

/* header */
.brand{left:145px;top:60px;display:flex;align-items:center;gap:12px;font-size:30px;font-weight:700;color:#111}
.brand-mark{width:26px;height:26px;background:#111}
.phone{right:145px;top:50px;font-size:26px;color:var(--navy);display:flex;align-items:center;gap:10px}
.nav{right:145px;top:122px;display:flex;gap:34px;font-size:14px;font-weight:600;color:#777;text-transform:uppercase}
.nav .active{color:var(--navy)}

/* hero */
.hero{left:0;top:168px;width:1200px;height:447px;background:linear-gradient(100deg,#c9ccd2 0%,#e4e6ea 35%,#f1f1f2 60%,#dfe1e4 100%)}
.hero-photo{left:0;top:0;width:700px;height:447px;background:linear-gradient(90deg,#b9bdc4 0%,#d9c6b3 35%,#c7b7a7 55%,#4e6487 75%,rgba(230,230,232,0) 100%)}
.hero-title{left:733px;top:32px;width:323px;text-align:center;font-size:23px;font-weight:700;line-height:1.35;color:#222}
.arrow{top:205px;width:20px;height:30px}
.calc{left:733px;top:107px;width:323px;height:300px;background:var(--blue);padding:12px 16px}
.calc h2{color:var(--white);font-size:23px;font-weight:700;margin-bottom:12px}
.field{height:38px;background:var(--white);margin-bottom:13px;display:flex;justify-content:space-between;align-items:center;padding:0 14px;font-size:13px;color:#333}
.field span:last-child{font-size:17px}
.field .small{font-size:13px!important}
.calc-btns{display:flex;gap:4px;margin-top:2px}
.calc-btns div{flex:1;height:36px;display:flex;align-items:center;justify-content:center;font-size:15px;font-weight:600;text-transform:uppercase}
.btn-calc{background:#262626;color:var(--white)}
.btn-clear{background:#333;color:#777}
.advanced{text-align:center;color:var(--white);font-size:13px;margin-top:8px}

/* welcome */
.welcome-img{left:145px;top:695px;width:323px;height:222px;background:linear-gradient(180deg,#2a3e78 0%,#5a6a9a 35%,#c78a4a 65%,#3aa3c8 85%,#7a5a3a 100%)}
.welcome-title{left:498px;top:685px;font-size:32px;font-weight:600;color:var(--navy)}
.welcome-text{left:498px;top:742px;width:560px;font-size:12.5px;line-height:1.75;color:#444}
.btn{background:var(--navy);color:var(--white);display:flex;align-items:center;justify-content:center;font-size:14px}
.read-more{left:498px;top:870px;width:103px;height:47px}

/* differ */
.differ{left:0;top:997px;width:1200px;height:500px;background:linear-gradient(180deg,#3b9ee0,#2a86d4)}
.section-title{width:1200px;text-align:center;font-size:32px;font-weight:600}
.differ-title{left:0;top:70px;color:var(--white)}
.card{top:136px;width:296px;height:282px;background:var(--white);text-align:center;padding:28px 24px 0}
.card svg{width:84px;height:84px;margin-bottom:18px}
.card p{font-size:14px;line-height:1.7;color:#444}

/* process */
.steps{left:140px;top:1568px;width:570px}
.step{display:flex;gap:22px;margin-bottom:26px}
.step svg{flex:0 0 56px;width:56px;height:56px}
.step p{font-size:16.5px;line-height:1.55;color:var(--navy)}
.process-img{left:733px;top:1577px;width:323px;height:463px;background:linear-gradient(180deg,#d8d8d6 0%,#ececea 40%,#b59a78 85%,#a88a66 100%)}

/* testimonials */
.testi{left:0;top:2120px;width:1200px;height:467px;background:linear-gradient(180deg,#1b4fb8,#1a48a6)}
.testi-title{left:0;top:68px;color:var(--white)}
.t-card{top:135px;width:292px;height:215px;background:var(--white);text-align:center;padding:18px 22px 0}
.t-card p{font-size:12.5px;line-height:1.65;color:#555}
.t-card h3{font-size:16px;font-weight:600;color:var(--navy);margin-top:14px}
.avatar{top:312px;width:80px;height:80px;border-radius:50%;background:radial-gradient(circle at 50% 40%,#d9b9a0,#6a5446);border:3px solid var(--white)}

/* contact */
.contact-title{left:0;top:2652px;color:var(--navy)}
.input{border:1px solid var(--line);background:var(--white);font-size:12px;color:#666;padding:0 20px;display:flex;align-items:center}
.input.msg{align-items:flex-start;padding-top:18px}
.submit{left:548px;top:2919px;width:104px;height:49px;font-size:15px}

/* footer */
.footer{left:0;top:3047px;width:1200px;height:305px;background:var(--footer);color:var(--white)}
.f-col h4{font-size:17px;font-weight:600;margin-bottom:10px}
.f-col li{list-style:none;font-size:11.5px;line-height:22.5px}
.partner{left:448px;top:90px;display:flex;align-items:center;gap:10px;font-size:20px;font-weight:700;color:#9ec6ef}
.partner-mark{width:22px;height:22px;background:#9ec6ef}
.news-input{left:836px;top:92px;width:218px;height:43px;background:#a9c7ea;color:#173d80;font-size:12px;display:flex;justify-content:space-between;align-items:center;padding:0 14px}
.f-rule{left:145px;top:226px;width:910px;height:1px;background:rgba(255,255,255,.35)}
.copyright{left:145px;top:256px;font-size:12px}
.social{right:145px;top:256px;display:flex;gap:18px}
.social span{width:14px;height:14px;border-radius:50%;background:var(--white)}
</style>
</head>
<body>

<header>
  <div class="abs brand"><span class="brand-mark"></span>Beacon Lending</div>
  <div class="abs phone">
    <svg width="20" height="20" viewBox="0 0 24 24"><path fill="#0a3c8f" d="M6.6 10.8a15.1 15.1 0 0 0 6.6 6.6l2.2-2.2c.3-.3.7-.4 1-.2 1.1.4 2.3.6 3.6.6.6 0 1 .4 1 1V20c0 .6-.4 1-1 1A17 17 0 0 1 3 4c0-.6.4-1 1-1h3.5c.6 0 1 .4 1 1 0 1.3.2 2.5.6 3.6.1.3 0 .7-.2 1z"/></svg>
    555 014 2290
  </div>
  <nav class="abs nav">
    <span class="active">Home</span><span>About Us</span><span>Our Process</span><span>Testimonials</span><span>Contact</span>
  </nav>
</header>

<section class="abs hero">
  <div class="abs hero-photo" role="img" aria-label="Smiling couple receiving house keys at the door of their new home"></div>
  <svg class="abs arrow" style="left:52px" viewBox="0 0 20 30"><path d="M15 4 5 15l10 11" stroke="#0a3c8f" stroke-width="4" fill="none"/></svg>
  <svg class="abs arrow" style="left:1126px" viewBox="0 0 20 30"><path d="M5 4l10 11-10 11" stroke="#0a3c8f" stroke-width="4" fill="none"/></svg>
  <h1 class="abs hero-title">FOCUS ON MENTORING<br>OUR CLIENTS INTO A HOME</h1>
  <form class="abs calc">
    <h2>MORTGAGE CALCULATOR</h2>
    <div class="field"><span>Mortgage Amount</span><span>$</span></div>
    <div class="field"><span>Mortgage Term</span><span class="small">Months</span></div>
    <div class="field"><span>Interest Rate</span><span>%</span></div>
    <div class="calc-btns"><div class="btn-calc">Calculate</div><div class="btn-clear">Clear</div></div>
    <div class="advanced">Advanced</div>
  </form>
</section>

<section class="welcome">
  <div class="abs welcome-img" role="img" aria-label="Modern house with lit pool at dusk"></div>
  <h2 class="abs welcome-title">Welcome to Beacon Lending</h2>
  <p class="abs welcome-text">Beacon Lending helps everyday buyers move from first questions to final keys. We review your credit, income and savings, explain every option in plain words, and build a clear plan before any lender looks at your file. Our team compares programs across many lenders so you see real choices, real rates and real next steps toward owning the home you want.</p>
  <div class="abs btn read-more">Read More</div>
</section>

<section class="abs differ">
  <h2 class="abs section-title differ-title">How we differ when buying a home?</h2>
  <div class="abs card" style="left:145px">
    <svg viewBox="0 0 84 84" fill="none" stroke="#0a3c8f" stroke-width="2.5"><rect x="22" y="14" width="40" height="26" rx="3"/><path d="M30 22h24M30 30h16"/><rect x="14" y="44" width="56" height="8"/><path d="M22 52v20M62 52v20M36 52v12h12V52"/></svg>
    <p>Sit with us before you with a lender. They will do a hard inquiry on your credit report and thus bring down your credit score just to tell you NO!</p>
  </div>
  <div class="abs card" style="left:452px">
    <svg viewBox="0 0 84 84" fill="none" stroke="#0a3c8f" stroke-width="2.5"><circle cx="42" cy="42" r="9"/><circle cx="18" cy="20" r="7"/><circle cx="66" cy="20" r="7"/><circle cx="18" cy="64" r="7"/><circle cx="66" cy="64" r="7"/><path d="M24 25l11 10M60 25 49 35M24 59l11-10M60 59 49 49"/></svg>
    <p>We work with all lenders and all brokers so we aren't biased. We utilize all of them so we can have access to all of the home programs available not just a few.</p>
  </div>
  <div class="abs card" style="left:759px">
    <svg viewBox="0 0 84 84" fill="none" stroke="#0a3c8f" stroke-width="2.5"><rect x="14" y="16" width="56" height="54" rx="4"/><path d="M14 30h56M26 10v12M58 10v12"/><circle cx="28" cy="42" r="3"/><circle cx="42" cy="42" r="3"/><circle cx="56" cy="42" r="3"/><circle cx="28" cy="56" r="3"/><path d="M40 56l4 4 8-8"/></svg>
    <p>Work with our consultants and our Agents to help get you approved today!</p>
  </div>
</section>

<section>
  <div class="abs steps">
    <div class="step">
      <svg viewBox="0 0 56 56" fill="none" stroke="#0a3c8f" stroke-width="2.2"><path d="M4 8h34v22H18l-8 8v-8H4z"/><path d="M42 18h10v22h-6v7l-7-7H22v-6"/><path d="M11 16h20M11 22h14"/></svg>
      <p>Are you trying to buy a home? Did you sit with a lender or broker and get denied?<br>We understand your pain. They just pulled a hard inquiry on your credit profile just to damage in further.</p>
    </div>
    <div class="step">
      <svg viewBox="0 0 56 56" fill="none" stroke="#0a3c8f" stroke-width="2.2"><circle cx="28" cy="28" r="23"/><path d="M17 28l8 8 15-16"/></svg>
      <p>Wouldn't you like to know if you can get approved before you damage your credit anymore?</p>
    </div>
    <div class="step">
      <svg viewBox="0 0 56 56" fill="none" stroke="#0a3c8f" stroke-width="2.2"><path d="M6 50h46M10 50V36h6v14M22 50V30h6v20M34 50V24h6v26M46 50V16h6v34"/><path d="M8 28l14-10 10 6 18-14"/></svg>
      <p>Call Beacon Lending today and talk to one of our agents, we can do a full financial analysis, pull your credit file, and figure out your DTI before you speak with a lender or broker.</p>
    </div>
    <div class="step">
      <svg viewBox="0 0 56 56" fill="none" stroke="#0a3c8f" stroke-width="2.2"><circle cx="28" cy="12" r="6"/><circle cx="14" cy="26" r="5"/><circle cx="42" cy="26" r="5"/><path d="M18 40c0-8 4-14 10-14s10 6 10 14M4 48c0-7 4-12 10-12M52 48c0-7-4-12-10-12M4 50h48"/></svg>
      <p>We also have an advantage! We work with every different lender/broker so we can offer you every program out there. Not just ones that are partners or let say "prefered vendors"</p>
    </div>
    <div class="step">
      <svg viewBox="0 0 56 56" fill="none" stroke="#0a3c8f" stroke-width="2.2"><circle cx="28" cy="28" r="9"/><path d="M28 4v8M28 44v8M4 28h8M44 28h8M11 11l6 6M39 39l6 6M45 11l-6 6M17 39l-6 6"/><circle cx="28" cy="28" r="17"/></svg>
      <p>Sit with Beacon Lending today! Let us worry about getting you approved before you waste you time/money and damage your credit any further!</p>
    </div>
  </div>
  <div class="abs process-img" role="img" aria-label="Agent showing a couple around a bright empty home interior"></div>
</section>

<section class="abs testi">
  <h2 class="abs section-title testi-title">Testimonials</h2>
  <svg class="abs arrow" style="left:52px;top:218px" viewBox="0 0 20 30"><path d="M15 4 5 15l10 11" stroke="#fff" stroke-width="3" fill="none"/></svg>
  <svg class="abs arrow" style="left:1126px;top:218px" viewBox="0 0 20 30"><path d="M5 4l10 11-10 11" stroke="#fff" stroke-width="3" fill="none"/></svg>
  <div class="abs t-card" style="left:145px"><p>They walked me through every step and never pulled my credit without asking. We closed on our first house in six weeks.</p><h3>Mark Ellis</h3></div>
  <div class="abs t-card" style="left:454px"><p>Honest advice, fast answers and a plan that actually worked. I finally understood my options before talking to a lender.</p><h3>Nora</h3></div>
  <div class="abs t-card" style="left:763px"><p>The team compared programs I never knew existed. Friendly, patient and clear from the first call to the closing table.</p><h3>Owen</h3></div>
  <div class="abs avatar" style="left:251px" role="img" aria-label="Portrait of client Mark Ellis"></div>
  <div class="abs avatar" style="left:560px" role="img" aria-label="Portrait of client Nora"></div>
  <div class="abs avatar" style="left:869px" role="img" aria-label="Portrait of client Owen"></div>
</section>

<section>
  <h2 class="abs section-title contact-title">Contact Us</h2>
  <div class="abs input" style="left:352px;top:2716px;width:240px;height:44px">Name</div>
  <div class="abs input" style="left:607px;top:2716px;width:240px;height:44px">Email</div>
  <div class="abs input msg" style="left:352px;top:2777px;width:495px;height:116px">Message</div>
  <div class="abs btn submit">SUBMIT</div>
</section>

<footer class="abs footer">
  <div class="abs f-col" style="left:145px;top:53px"><h4>Resources</h4><ul><li>First Steps</li><li>Credit Basics</li><li>Loan Types</li><li>Down Payment</li><li>FAQ</li></ul></div>
  <div class="abs f-col" style="left:296px;top:53px"><h4>Tools</h4><ul><li>Calculators</li><li>Rate Guide</li><li>Budget Planner</li><li>Checklists</li><li>Glossary</li></ul></div>
  <div class="abs f-col" style="left:450px;top:53px"><h4>Partners</h4></div>
  <div class="abs partner"><span class="partner-mark"></span>KeyStep Ready</div>
  <div class="abs f-col" style="left:698px;top:53px"><h4>Menu</h4><ul><li>Home</li><li>About Us</li><li>Our Process</li><li>Testimonials</li><li>Contact</li></ul></div>
  <div class="abs f-col" style="left:836px;top:53px"><h4>Newsletter</h4></div>
  <div class="abs news-input"><span>Email Address</span>
    <svg width="20" height="15" viewBox="0 0 20 15"><rect width="20" height="15" fill="#173d80"/><path d="M1 1l9 7 9-7" stroke="#a9c7ea" stroke-width="1.5" fill="none"/></svg>
  </div>
  <div class="abs f-rule"></div>
  <div class="abs copyright">Copyright © 2019 Beacon Lending. All rights reserved.</div>
  <div class="abs social"><span></span><span></span><span></span></div>
</footer>

</body>
</html>
```